Brightwell - Self Development Mobile App

Basic Instructions
1. please create an android app screen design for me, in figma, for my new app “Brightwell” based on this pencil drawing (Subjects.jpg)
2. Create the color pallet based on the colors of the logo (#fcd354 and #5dc9b7) and also add shades based on these colors based on material design.
3. the background should be white.
4. Use material design
Get Inspired by parlavox design and calmreed design
These are the directions i provided for the programmer on how this screen will work:
top bar:
back icon on left (show if you are in a category and press to go back one category)
name of the field in middle in bold
share icon for sharing the current subject on the right before the drop down menu
3 dot icon on the right (drop down menu)
2nd top bar:
fire icon on left for streak (how many days straight did you do a lesson)
star icon a bit after it (how many lessons did you pass)
circles section:
each category will get a section
each category will have a small star with a number that shows how many stars the user has from that category
each category will have an icon before it
under each category there will be circles for all the subjects under that category
scroll horizontally to see more subjects
each subject will have the amount stars gained from it (like the circles of the fields in the fields screen)
scroll down to see more fields with their subjects
note that the order of the subjects and categories should be based on the practial/spiritual score that the user has been assigned based on the initial wizard
More Notes
1. the scribbles in the circles under the following categories (Dreams, Sub-Concious, Feeling)) are just place filers. Please add example content based on the content in the circles that are under “Memory” category
2. There are more sections after Feeling so users should be able to scroll down to see more sections
3. There are more categories to the right so under each section
Final Thoughts
Maybe its better to have rounded cornered squares instead of circles. You choose what you think is best.
After you have created the Subjects screen and I like it, then I'll give you instructions for the other 5 screens.
general public, adults 18-80

```html
<!DOCTYPE html>
<html lang="en">
<head>
<meta charset="utf-8">
<title>Brightwell – App Screens</title>
<link href="https://fonts.googleapis.com/css2?family=Mukta:wght@400;500;600;700;800&display=swap" rel="stylesheet">
<style>
:root{
  --yellow:#fcd354;
  --yellow-soft:#fdf0c8;
  --teal:#5dc9b7;
  --teal-dark:#3ea693;
  --teal-deep:#2f9784;
  --mint:#eef8f6;
  --mint-bg:#f3faf9;
  --line:#e2f2ef;
  --ink:#4a4a4a;
  --ink-soft:#5e5e5e;
  --stage:#0e0e0e;
  --white:#ffffff;
}
*{box-sizing:border-box;margin:0;padding:0}
html,body{width:1200px;height:857px;overflow:hidden;background:var(--stage)}
body{font-family:"Mukta",sans-serif;color:var(--ink)}
.stage{position:absolute;left:0;top:0;width:1400px;height:1000px;transform:scale(.857143);transform-origin:0 0}
.screen{position:absolute;top:52px;width:414px;height:896px;border-radius:40px;overflow:hidden;background:var(--mint-bg)}
.screen--fields{left:39px}.screen--mind{left:493px}.screen--wizard{left:947px}
.header-art{position:absolute;left:0;top:0;width:100%;height:246px;background:linear-gradient(135deg,var(--teal-dark) 0%,var(--teal) 55%,var(--teal-dark) 100%)}
.brand{position:absolute;left:0;right:0;top:22px;text-align:center;font-weight:800;font-size:38px;letter-spacing:.5px;color:var(--yellow)}
.brand-rule{position:absolute;left:30px;right:30px;top:84px;height:1px;background:var(--yellow);opacity:.7}
.round-btn{position:absolute;top:102px;width:34px;height:34px;border-radius:50%;background:var(--yellow);display:flex;align-items:center;justify-content:center}
.round-btn svg{width:14px;height:14px}
.btn-back{left:26px}.btn-share{left:312px}.btn-menu{left:354px}
.screen-title{position:absolute;left:0;right:0;top:103px;text-align:center;font-weight:700;font-size:23px;color:var(--yellow)}
.card{position:absolute;left:26px;top:160px;width:362px;height:641px;background:var(--white);border-radius:28px;box-shadow:0 14px 30px rgba(0,0,0,.05)}
.stats{position:absolute;left:26px;top:14px;display:flex;gap:16px;font-weight:700;font-size:17px}
.stats span{display:flex;align-items:center;gap:5px}
.stats svg{width:15px;height:15px}
.stat-streak{color:var(--yellow)}.stat-stars{color:var(--teal)}
.bottom-nav{position:absolute;left:0;right:0;bottom:0;height:72px;background:var(--white);display:flex;align-items:center;padding-left:26px}
.nav-item{display:flex;align-items:center;gap:12px;font-size:15px;color:var(--ink-soft);height:34px}
.nav-item + .nav-item{border-left:1px solid #dedede;margin-left:22px;padding-left:22px}
.nav-icon{width:36px;height:36px;border-radius:8px;background:var(--teal);display:flex;align-items:center;justify-content:center}
.nav-icon svg{width:20px;height:20px}
/* fields grid */
.tile{position:absolute;width:143px;height:124px;border-radius:16px;border:1px solid var(--line);background:var(--white)}
.tile--active{background:var(--teal);border-color:var(--teal)}
.tile-icon{position:absolute;left:22px;top:20px;width:58px;height:58px;border-radius:12px;background:var(--yellow)}
.tile-score{position:absolute;left:95px;top:20px;width:26px;height:58px;border-radius:4px;background:var(--mint);display:flex;flex-direction:column;align-items:center;padding-top:10px;gap:6px;font-size:12px;font-weight:600;color:var(--teal)}
.tile--active .tile-score{background:rgba(255,255,255,.18)}
.tile-score svg{width:14px;height:14px}
.tile-label{position:absolute;left:22px;top:89px;font-weight:700;font-size:16px;color:var(--ink-soft)}
.tile--active .tile-label{color:var(--white)}
/* mind list */
.cat-icon{position:absolute;left:22px;width:50px;height:50px;border-radius:12px;background:var(--yellow)}
.cat-icon--open{background:var(--teal)}
.cat-name{position:absolute;left:90px;font-weight:700;font-size:16px;color:var(--ink-soft)}
.chev{position:absolute;left:327px;width:14px;height:14px}
.lesson{position:absolute;left:91px;width:248px;height:43px;border-radius:6px;background:var(--mint);display:flex;align-items:center;justify-content:space-between;padding:0 22px 0 20px;font-size:14px;color:var(--ink-soft)}
.lesson-score{display:flex;align-items:center;gap:7px;font-weight:700;font-size:14px;color:var(--teal)}
.lesson-score svg{width:13px;height:13px}
/* wizard */
.prompt{position:absolute;left:0;right:0;top:32px;text-align:center;font-weight:600;font-size:16px;line-height:28px;color:var(--ink-soft)}
.chip{position:absolute;height:42px;border-radius:5px;background:var(--mint);color:var(--teal);font-size:16px;display:flex;align-items:center;justify-content:center}
.chip--selected{background:var(--teal);color:var(--white)}
.progress{position:absolute;left:40px;top:475px;width:283px;height:12px;border-radius:6px;background:var(--yellow-soft)}
.progress-fill{position:absolute;left:0;top:0;width:47px;height:12px;border-radius:6px;background:var(--yellow)}
.progress-knob{position:absolute;left:40px;top:-1px;width:14px;height:14px;border-radius:50%;background:var(--teal)}
.progress-label{position:absolute;left:48px;top:502px;font-size:14px;color:var(--ink-soft)}
</style>
</head>
<body>
<svg width="0" height="0" style="position:absolute">
  <defs>
    <symbol id="star" viewBox="0 0 24 24"><path fill="currentColor" d="M12 2l2.9 6.6 7.1.6-5.4 4.7 1.6 7-6.2-3.8-6.2 3.8 1.6-7L2 9.2l7.1-.6z"/></symbol>
    <symbol id="chev-down" viewBox="0 0 14 14"><path d="M2 4.5l5 5 5-5" fill="none" stroke="#4a4a4a" stroke-width="2" stroke-linecap="round" stroke-linejoin="round"/></symbol>
    <symbol id="chev-up" viewBox="0 0 14 14"><path d="M2 9.5l5-5 5 5" fill="none" stroke="#4a4a4a" stroke-width="2" stroke-linecap="round" stroke-linejoin="round"/></symbol>
    <symbol id="back" viewBox="0 0 14 14"><path d="M9 3L5 7l4 4" fill="none" stroke="#e0a91c" stroke-width="1.6" stroke-linecap="round" stroke-linejoin="round"/></symbol>
    <symbol id="share" viewBox="0 0 14 14"><g fill="#d4961a"><circle cx="10.5" cy="3" r="2"/><circle cx="3.5" cy="7" r="2"/><circle cx="10.5" cy="11" r="2"/></g><path d="M10.5 3L3.5 7l7 4" stroke="#d4961a" stroke-width="1.2" fill="none"/></symbol>
    <symbol id="menu" viewBox="0 0 14 14"><g fill="#d4961a"><rect x="2" y="3" width="10" height="2" rx="1"/><rect x="2" y="6" width="10" height="2" rx="1"/><rect x="2" y="9" width="10" height="2" rx="1"/></g></symbol>
    <symbol id="home" viewBox="0 0 20 20"><path d="M10 2L1.5 9.5h2.5V18h4.5v-5h3v5H16V9.5h2.5z" fill="#fff"/></symbol>
    <symbol id="compass" viewBox="0 0 20 20"><circle cx="10" cy="10" r="8.5" fill="#fff"/><path d="M13.5 6.5L11.3 11.3 6.5 13.5 8.7 8.7z" fill="#5dc9b7"/></symbol>
    <symbol id="user" viewBox="0 0 20 20"><circle cx="10" cy="6" r="4" fill="#fff"/><path d="M2.5 18.5c0-4.5 3.3-7 7.5-7s7.5 2.5 7.5 7z" fill="#fff"/></symbol>
  </defs>
</svg>

<main class="stage">

  <!-- Fields screen -->
  <section class="screen screen--fields">
    <div class="header-art" role="img" aria-label="Teal header with a faint hexagon network pattern"></div>
    <h1 class="brand">BRIGHTWELL</h1>
    <div class="brand-rule"></div>
    <span class="round-btn btn-back"><svg><use href="#back"/></svg></span>
    <span class="round-btn btn-share"><svg><use href="#share"/></svg></span>
    <span class="round-btn btn-menu"><svg><use href="#menu"/></svg></span>

    <div class="card">
      <div class="stats">
        <span class="stat-streak"><svg><use href="#star"/></svg>02</span>
        <span class="stat-stars"><svg><use href="#star"/></svg>34</span>
      </div>

      <div class="tile tile--active" style="left:26px;top:55px">
        <div class="tile-icon" role="img" aria-label="Brain icon"></div>
        <div class="tile-score" style="color:var(--yellow)"><svg><use href="#star"/></svg></div>
        <div class="tile-label">Mind</div>
      </div>
      <div class="tile" style="left:193px;top:55px">
        <div class="tile-icon" role="img" aria-label="Thumbs-up speech bubble icon"></div>
        <div class="tile-score"><svg><use href="#star"/></svg>04</div>
        <div class="tile-label">Reccomended</div>
      </div>
      <div class="tile" style="left:26px;top:198px">
        <div class="tile-icon" role="img" aria-label="Body figure icon"></div>
        <div class="tile-score"><svg><use href="#star"/></svg>02</div>
        <div class="tile-label">Body</div>
      </div>
      <div class="tile" style="left:193px;top:198px">
        <div class="tile-icon" role="img" aria-label="Finance growth icon"></div>
        <div class="tile-score"><svg><use href="#star"/></svg></div>
        <div class="tile-label">Finance</div>
      </div>
      <div class="tile" style="left:26px;top:341px">
        <div class="tile-icon" role="img" aria-label="Professional with briefcase icon"></div>
        <div class="tile-score"><svg><use href="#star"/></svg></div>
        <div class="tile-label">Proffessional</div>
      </div>
      <div class="tile" style="left:193px;top:341px">
        <div class="tile-icon" role="img" aria-label="Social media bubbles icon"></div>
        <div class="tile-score"><svg><use href="#star"/></svg>17</div>
        <div class="tile-label">Social</div>
      </div>
      <div class="tile" style="left:26px;top:484px">
        <div class="tile-icon" role="img" aria-label="Meditation lotus icon"></div>
        <div class="tile-score"><svg><use href="#star"/></svg></div>
        <div class="tile-label">Spiritual</div>
      </div>
      <div class="tile" style="left:193px;top:484px">
        <div class="tile-icon" role="img" aria-label="Hobbies activities icon"></div>
        <div class="tile-score"><svg><use href="#star"/></svg>41</div>
        <div class="tile-label">Hobbies</div>
      </div>
    </div>

    <nav class="bottom-nav">
      <span class="nav-item"><span class="nav-icon"><svg><use href="#home"/></svg></span>Fields</span>
      <span class="nav-item"><span class="nav-icon"><svg><use href="#compass"/></svg></span>Explore</span>
      <span class="nav-item"><span class="nav-icon"><svg><use href="#user"/></svg></span>Account</span>
    </nav>
  </section>

  <!-- Mind screen -->
  <section class="screen screen--mind">
    <div class="header-art" role="img" aria-label="Teal header with a faint hexagon network pattern"></div>
    <h1 class="brand">BRIGHTWELL</h1>
    <div class="brand-rule"></div>
    <span class="round-btn btn-back"><svg><use href="#back"/></svg></span>
    <h2 class="screen-title">MIND</h2>
    <span class="round-btn btn-share"><svg><use href="#share"/></svg></span>
    <span class="round-btn btn-menu"><svg><use href="#menu"/></svg></span>

    <div class="card">
      <div class="stats">
        <span class="stat-streak"><svg><use href="#star"/></svg>02</span>
        <span class="stat-stars"><svg><use href="#star"/></svg>34</span>
      </div>

      <div class="cat-icon cat-icon--open" style="top:54px" role="img" aria-label="Brain icon"></div>
      <div class="cat-name" style="top:48px">Memories</div>
      <svg class="chev" style="top:52px"><use href="#chev-up"/></svg>

      <div class="lesson" style="top:83px">Basic Memory<span class="lesson-score"><svg><use href="#star"/></svg>02</span></div>
      <div class="lesson" style="top:136px">Names<span class="lesson-score"><svg><use href="#star"/></svg>01</span></div>
      <div class="lesson" style="top:190px">Numbers<span class="lesson-score"><svg><use href="#star"/></svg>04</span></div>
      <div class="lesson" style="top:243px">Lorem Lipsum<span class="lesson-score"><svg><use href="#star"/></svg>04</span></div>

      <div class="cat-icon" style="top:314px" role="img" aria-label="Dreaming head icon"></div>
      <div class="cat-name" style="top:328px">Dreams</div>
      <svg class="chev" style="top:329px"><use href="#chev-down"/></svg>

      <div class="cat-icon" style="top:379px" role="img" aria-label="Sub-conscious brain and heart icon"></div>
      <div class="cat-name" style="top:393px">Sub-Concious</div>
      <svg class="chev" style="top:396px"><use href="#chev-down"/></svg>

      <div class="cat-icon" style="top:443px" role="img" aria-label="Feelings icon"></div>
      <div class="cat-name" style="top:457px">Feeling</div>
      <svg class="chev" style="top:461px"><use href="#chev-down"/></svg>
    </div>

    <nav class="bottom-nav">
      <span class="nav-item"><span class="nav-icon"><svg><use href="#home"/></svg></span>Fields</span>
      <span class="nav-item"><span class="nav-icon"><svg><use href="#compass"/></svg></span>Explore</span>
      <span class="nav-item"><span class="nav-icon"><svg><use href="#user"/></svg></span>Account</span>
    </nav>
  </section>

  <!-- Wizard screen -->
  <section class="screen screen--wizard">
    <div class="header-art" role="img" aria-label="Teal header with a faint hexagon network pattern"></div>
    <h1 class="brand">BRIGHTWELL</h1>
    <div class="brand-rule"></div>
    <span class="round-btn btn-back"><svg><use href="#back"/></svg></span>
    <h2 class="screen-title">WIZARD</h2>
    <span class="round-btn btn-share"><svg><use href="#share"/></svg></span>
    <span class="round-btn btn-menu"><svg><use href="#menu"/></svg></span>

    <div class="card">
      <p class="prompt">Please choose three subject that<br>interest you most:</p>

      <span class="chip chip--selected" style="left:39px;top:99px;width:118px">Mind</span>
      <span class="chip" style="left:174px;top:99px;width:148px">Reccomended</span>
      <span class="chip" style="left:39px;top:158px;width:88px">Body</span>
      <span class="chip" style="left:138px;top:158px;width:88px">Finance</span>
      <span class="chip" style="left:238px;top:158px;width:84px">Social</span>
      <span class="chip" style="left:39px;top:218px;width:88px">Hobbies</span>
      <span class="chip" style="left:138px;top:218px;width:88px">Spiritual</span>
      <span class="chip" style="left:238px;top:218px;width:84px">Mind</span>
      <span class="chip" style="left:39px;top:277px;width:148px">Proffessional</span>

      <div class="progress"><div class="progress-fill"></div><div class="progress-knob"></div></div>
      <div class="progress-label">01/08</div>
    </div>

    <nav class="bottom-nav">
      <span class="nav-item"><span class="nav-icon"><svg><use href="#home"/></svg></span>Fields</span>
      <span class="nav-item"><span class="nav-icon"><svg><use href="#compass"/></svg></span>Explore</span>
      <span class="nav-item"><span class="nav-icon"><svg><use href="#user"/></svg></span>Account</span>
    </nav>
  </section>

</main>
</body>
</html>
```